Design for "Quiver" protein health bars wrappers

I need a new design for a protein bar that my partners and I are launching for the North American and European markets.
The bar's name is "Quiver."
Given the masculine/aggressive nature of that name, we are thinking of neutralizing it with a more feminine/soft font and design. But hey - the sky is the limit. We obviously want this 20-gram protein bar to sell to a wide net (not just men but women also). So if it means having a Zephyr Panel font/design (or whatever) in order to do this, so be it. I leave it up to your intelligence and experience.

The official name of the bar is just "QUIVER" (not "Quiver Protein").

We have six flavors divided into two categories, which are 1) SOFT and 2) CRUNCHY.
So, the idea is to make two similar designs for the wrapper that still distinguish themselves from each other because one is 'soft' and the other is 'crunchy.'
Then, within each category, the idea is to have three color variations, designating the three flavors in each category.

Please look at the dimensions and examples of the generic wrapper designs that we already have (and which we find too generic), which I have uploaded.

Target Market(s)

North America - Valmart, Green Basket
Europe - Norway, Sweden, Denmark, Germany, France, Switzerland, Italy.

Industry/Entity Type

Nutrition

Logo Text

Quiver

Font styles to use
Serif
Decorative

Colors
fff6dc
f04a50

Requirements
Must have
• The title is "Quiver".
• We have six flavors divided into two categories, which are 1) SOFT and 2) CRUNCHY.
• You can work on the two different types of similar-but-different designs for the "soft" and for the "cruncy." Then it's just a question of color variations for each flavor.
• The flavors are:
• SOFT: 1) strawberry, 2) Chocolate brownie, 3) Cinnamon Crunch
• CRUNCY: 1) Peanut, 2) Lemon, 3) Coconut.
• On the side or at the bottom, there should be stated:
• "20 gm protein"
• "children friendly"
Nice to have
• Obvious: a design that catches the eye and inspires someone to buy the bar to eat it.
• Part of the design could include a photograph of the actual bar (you can use generic photos for that until we place a pic of the actual bar). Like 1/4th of the total surface (or even a little smaller).

```html
<!DOCTYPE html>
<html lang="en">
<head>
<meta charset="utf-8">
<title>Quiver protein bar wrappers</title>
<link rel="stylesheet" href="https://fonts.googleapis.com/css2?family=Bebas+Neue&family=Caveat+Brush&family=Oswald:wght@500&display=swap">
<style>
  :root {
    --backdrop: #1d1d1d;
    --wrapper-white: #ffffff;
    --crimp-grey: #d9d9d9;
    --crimp-line: #b9b9b9;
    --cinnamon-pill: #cf8f5c;
    --cinnamon-deep: #5a1b10;
    --cinnamon-photo-a: #7a4a2c;
    --cinnamon-photo-b: #b9784a;
    --strawberry: #c1222f;
    --strawberry-photo-a: #8e1119;
    --strawberry-photo-b: #d9363c;
    --brownie: #4b1b12;
    --brownie-photo-a: #2e140c;
    --brownie-photo-b: #5a2c1c;
  }
  * { box-sizing: border-box; margin: 0; padding: 0; }
  html, body { width: 1200px; height: 1056px; overflow: hidden; background: var(--backdrop); }
  .canvas { position: relative; width: 1200px; height: 1056px; }

  .wrapper {
    position: absolute; width: 700px; height: 324px;
    background: var(--wrapper-white);
    overflow: hidden;
  }
  .wrapper--cinnamon { left: 308px; top: 36px; --accent: var(--cinnamon-deep); --pill: var(--cinnamon-pill); --photo-a: var(--cinnamon-photo-a); --photo-b: var(--cinnamon-photo-b); }
  .wrapper--strawberry { left: 134px; top: 366px; --accent: var(--strawberry); --pill: var(--strawberry); --photo-a: var(--strawberry-photo-a); --photo-b: var(--strawberry-photo-b); }
  .wrapper--brownie { left: 334px; top: 690px; --accent: var(--brownie); --pill: var(--brownie); --photo-a: var(--brownie-photo-a); --photo-b: var(--brownie-photo-b); }

  .crimp {
    position: absolute; top: 0; bottom: 0; width: 44px;
    background: repeating-linear-gradient(180deg, var(--crimp-grey) 0 4px, var(--crimp-line) 4px 5px);
  }
  .crimp--left { left: 0; }
  .crimp--right { right: 0; }

  .badges { position: absolute; left: 68px; top: 52px; display: flex; }
  .badge {
    width: 40px; height: 40px; border-radius: 50%;
    border: 2px solid var(--accent); background: var(--wrapper-white);
    display: flex; flex-direction: column; align-items: center; justify-content: center;
    font-family: 'Oswald', sans-serif; color: var(--accent); line-height: 1;
    text-align: center;
  }
  .badge + .badge { margin-left: -4px; }
  .badge__small { font-size: 6px; }
  .badge__value { font-size: 10px; margin-top: 2px; }
  .badge--protein .badge__small { background: var(--accent); color: var(--wrapper-white); padding: 1px 2px; }
  .badge__heart { width: 9px; height: 8px; margin-bottom: 2px; }

  .flavor-pill {
    position: absolute; left: 154px; top: 24px; height: 40px;
    padding: 0 20px; border-radius: 20px;
    background: var(--pill); color: var(--wrapper-white);
    font-family: 'Caveat Brush', cursive; font-size: 30px; line-height: 40px;
    transform: rotate(-3deg); transform-origin: left center;
  }

  .brand-name {
    position: absolute; left: 170px; top: 62px;
    font-family: 'Bebas Neue', sans-serif; font-size: 205px; line-height: 1;
    color: var(--accent); letter-spacing: 2px;
    transform: rotate(-4deg); transform-origin: left bottom;
  }

  .bar-photo {
    position: absolute; left: 200px; right: 44px; bottom: 12px; height: 72px;
    background: linear-gradient(90deg, var(--photo-a), var(--photo-b));
    clip-path: polygon(0 70%, 30% 40%, 60% 15%, 100% 0, 100% 100%, 0 100%);
  }
</style>
</head>
<body>
<main class="canvas">

  <section class="wrapper wrapper--cinnamon" aria-label="Quiver Cinnamon Crunch wrapper">
    <div class="crimp crimp--left"></div>
    <div class="crimp crimp--right"></div>
    <div class="badges">
      <div class="badge badge--protein"><span class="badge__small">PROTEIN</span><span class="badge__value">20gr</span></div>
      <div class="badge badge--kids">
        <svg class="badge__heart" viewBox="0 0 10 9"><path d="M5 9 L0.8 4.6 A2.3 2.3 0 0 1 5 1.6 A2.3 2.3 0 0 1 9.2 4.6 Z" fill="currentColor"/></svg>
        <span class="badge__small">CHILDREN<br>FRIENDLY</span>
      </div>
    </div>
    <div class="flavor-pill">Cinnamon Crunch</div>
    <div class="brand-name">QUIVER</div>
    <div class="bar-photo" role="img" aria-label="Photo of a cinnamon crunch protein bar"></div>
  </section>

  <section class="wrapper wrapper--strawberry" aria-label="Quiver Strawberry wrapper">
    <div class="crimp crimp--left"></div>
    <div class="crimp crimp--right"></div>
    <div class="badges">
      <div class="badge badge--protein"><span class="badge__small">PROTEIN</span><span class="badge__value">20gr</span></div>
      <div class="badge badge--kids">
        <svg class="badge__heart" viewBox="0 0 10 9"><path d="M5 9 L0.8 4.6 A2.3 2.3 0 0 1 5 1.6 A2.3 2.3 0 0 1 9.2 4.6 Z" fill="currentColor"/></svg>
        <span class="badge__small">CHILDREN<br>FRIENDLY</span>
      </div>
    </div>
    <div class="flavor-pill">Strawberry</div>
    <div class="brand-name">QUIVER</div>
    <div class="bar-photo" role="img" aria-label="Photo of fresh strawberries"></div>
  </section>

  <section class="wrapper wrapper--brownie" aria-label="Quiver Chocolate Brownie wrapper">
    <div class="crimp crimp--left"></div>
    <div class="crimp crimp--right"></div>
    <div class="badges">
      <div class="badge badge--protein"><span class="badge__small">PROTEIN</span><span class="badge__value">20gr</span></div>
      <div class="badge badge--kids">
        <svg class="badge__heart" viewBox="0 0 10 9"><path d="M5 9 L0.8 4.6 A2.3 2.3 0 0 1 5 1.6 A2.3 2.3 0 0 1 9.2 4.6 Z" fill="currentColor"/></svg>
        <span class="badge__small">CHILDREN<br>FRIENDLY</span>
      </div>
    </div>
    <div class="flavor-pill">Chocolate Brownie</div>
    <div class="brand-name">QUIVER</div>
    <div class="bar-photo" role="img" aria-label="Photo of a chocolate brownie bar"></div>
  </section>

</main>
</body>
</html>
```